New landing page for book

Redesign http://www.quandelfieldworks.com so it looks more cutting edge and perhaps have buttons for the online bookstores.

Also I may soon have a trailer video produced so it Would be great to see an option with space for where a video might go and an option as the site is now without a video. Thanks

Industry/Entity Type

Online

Number of Pages Required

1 page

Colors

Designer to choose colors to be used in the design.

```html
<!DOCTYPE html>
<html lang="en">
<head>
<meta charset="utf-8">
<title>Vrelska — International Financial Crime Thriller</title>
<link rel="stylesheet" href="https://fonts.googleapis.com/css2?family=Oswald:wght@500;600;700&family=Roboto+Condensed:wght@400;700&display=swap">
<style>
:root{
  --ink:#4a2a22;
  --accent:#e9652a;
  --header:#231a17;
  --teal-dark:#1d4a45;
  --mint:#b3e2d1;
  --sage:#5f8579;
  --dot:#57b596;
  --footer:#0d0f0e;
  --white:#ffffff;
  --border:#c9c9c9;
}
*{box-sizing:border-box;margin:0;padding:0}
html,body{width:1105px;height:1200px;overflow:hidden;background:var(--white)}
body{position:relative;font-family:"Roboto Condensed",sans-serif;color:var(--ink)}
.hero-backdrop{position:absolute;left:0;top:0;width:1105px;height:394px;
  background:linear-gradient(90deg,#6b4a34 0%,#8a6146 18%,#5a3a2b 45%,#3a221c 75%,#241613 100%)}
.site-header{position:absolute;left:0;top:21px;width:1105px;height:46px;background:rgba(30,22,19,.92)}
.site-title{position:absolute;left:139px;top:12px;font-family:"Oswald",sans-serif;font-weight:600;font-size:16px;color:var(--white);letter-spacing:.2px}
.site-nav{position:absolute;right:173px;top:12px;display:flex;gap:14px;font-family:"Oswald",sans-serif;font-weight:600;font-size:16px;color:var(--white)}
.site-nav .caret{font-size:8px;vertical-align:top;margin-left:6px}
.book-cover{position:absolute;left:138px;top:94px;width:217px;height:342px;
  background:linear-gradient(180deg,#4a3a30 0%,#7a5838 35%,#b8672e 60%,#3c5a52 85%,#1e3d3a 100%)}
.buy-band{position:absolute;left:138px;top:436px;width:217px;height:56px;background:var(--teal-dark);
  color:var(--white);font-family:"Oswald",sans-serif;font-weight:600;font-size:36px;text-align:center;line-height:56px;letter-spacing:.5px}
.store-grid{position:absolute;left:138px;top:504px;display:grid;grid-template-columns:103px 103px;column-gap:11px;row-gap:11px}
.store-btn{height:46px;border:1px solid var(--border);background:var(--white);display:flex;align-items:center;justify-content:center;gap:6px;
  font-family:"Roboto Condensed",sans-serif;font-weight:700;font-size:16px;color:#2b2b2b}
.store-btn .mark{width:12px;height:12px;background:#2b2b2b}
.store-btn .mark.round{border-radius:50%}
.video{position:absolute;left:405px;top:93px;width:513px;height:285px;background:#000}
.video-frame{position:absolute;left:0;top:37px;width:513px;height:215px;
  background:linear-gradient(135deg,#3f4a3c 0%,#6a4e4c 40%,#8a5a5a 60%,#3e5a40 100%)}
.video-controls{position:absolute;left:0;top:252px;width:513px;height:33px}
.play{position:absolute;left:236px;top:130px}
.intro{position:absolute;left:385px;top:420px;width:540px}
.headline{font-family:"Oswald",sans-serif;font-weight:600;font-size:21px;line-height:25px;color:var(--ink);text-transform:uppercase;letter-spacing:-.2px}
.headline .title{color:var(--accent)}
.lead{margin-top:20px;font-weight:700;font-size:10.5px;line-height:13px}
.intro p.body{margin-top:9px;font-size:9px;line-height:12px}
.intro p.lead + p.body{margin-top:13px}
.closing{margin-top:12px;font-weight:700;font-size:10.5px;line-height:13px}
.reviews{position:absolute;left:0;top:734px;width:1105px;height:419px;
  background:radial-gradient(ellipse at 50% 40%,#1f302c 0%,#152320 55%,#0e1715 100%)}
.reviews h2{position:absolute;left:0;top:52px;width:1105px;text-align:center;font-family:"Oswald",sans-serif;font-weight:700;font-size:36px;color:var(--white);letter-spacing:.3px}
.card{position:absolute;text-align:center}
.card.side{top:152px;width:217px;height:157px;background:rgba(95,133,121,.92);color:#233632;font-size:9.5px;line-height:14px;overflow:hidden}
.card.left{left:138px}
.card.right{left:749px}
.card .quote{position:absolute;top:52px;width:300px}
.card.left .quote{left:5px}
.card.right .quote{left:-90px}
.card .cite{position:absolute;top:117px;font-weight:700;font-size:10px}
.card.left .cite{left:0;width:211px}
.card.right .cite{left:0;width:120px}
.card.main{left:356px;top:133px;width:393px;height:182px;background:var(--mint);color:#3a5650}
.card.main .quote{left:50px;top:60px;width:293px;font-size:11.5px;line-height:16.5px}
.card.main .qm{font-family:"Oswald",sans-serif;font-weight:700;font-size:16px;color:#3a5650}
.card.main .cite{left:0;width:393px;top:140px;font-size:11px}
.bubble{position:absolute;left:514px;top:112px}
.dots{position:absolute;left:516px;top:348px;display:flex;gap:9px}
.dots span{width:12px;height:12px;border-radius:50%;background:var(--dot)}
.dots span.active{background:transparent;border:1.5px solid var(--white)}
.site-footer{position:absolute;left:0;top:1153px;width:1105px;height:47px;background:var(--footer);
  color:#cfcfcf;font-size:8px;text-align:center;line-height:47px;letter-spacing:.2px}
.to-top{position:absolute;left:918px;top:1143px;width:37px;height:37px;border-radius:50%;background:#2d2d2d}
</style>
</head>
<body>
<div class="hero-backdrop" role="img" aria-label="Moody sepia photograph of a city street at dusk"></div>

<header class="site-header">
  <div class="site-title">INTERNATIONAL FINANCIAL CRIME THRILLER</div>
  <nav class="site-nav"><span>BUY NOW<span class="caret">▼</span></span><span>CONTACT</span></nav>
</header>

<div class="book-cover" role="img" aria-label="Book cover of Vrelska by Marek Dunholt: an armed operative before a capitol dome"></div>
<div class="buy-band">BUY NOW!</div>

<div class="store-grid">
  <div class="store-btn">Amberly</div>
  <div class="store-btn">Hollis &amp; Pike</div>
  <div class="store-btn"><span class="mark"></span>Fieldplay</div>
  <div class="store-btn"><span class="mark"></span>Pagebox</div>
  <div class="store-btn"><span class="mark round"></span>Tandem</div>
  <div class="store-btn"><span class="mark"></span>Inkmill</div>
</div>

<div class="video">
  <div class="video-frame" role="img" aria-label="Trailer still: stock ticker figures projected over a dim scene"></div>
  <svg class="play" width="41" height="29" viewBox="0 0 41 29"><rect width="41" height="29" rx="6" fill="#1e1e1e" fill-opacity=".85"/><path d="M16 9 L26 14.5 L16 20 Z" fill="#fff"/></svg>
  <svg class="video-controls" width="513" height="33" viewBox="0 0 513 33"><rect x="12" y="15" width="492" height="3" rx="1.5" fill="#8a8a8a"/><circle cx="23" cy="16.5" r="5.5" fill="#d8d8d8"/></svg>
</div>

<section class="intro">
  <h1 class="headline"><span class="title">Vrelska:</span> ATMs have shuttered. Stock markets have gone haywire. Can one operative stop a deadly band of criminals before it is too late?</h1>
  <p class="lead">When Anselm Krauth is asked to investigate a devastating cyber-attack, he is drawn into a conspiracy that threatens not only his own life, but the entire United States’ economy...</p>
  <p class="body">German intelligence operative Anselm Krauth has been asked to investigate the cyber crime gang who sparked massive unrest in Kenya by taking over electronic transactions. But as he digs deeper, a wiretap on hacker communications reveals this is only the beginning.</p>
  <p class="body">Vrelska, a shadowy criminal cabal, has launched a massive cyber attack on the United States.</p>
  <p class="body">Taking off for Washington, Krauth unexpectedly teams up with American gun for hire, Jory Vandermeer, and dives head-first into a massive conspiracy that reaches all the way up to the very top of the U.S. Government.</p>
  <p class="body">Stock markets have gone haywire. ATMs have shuttered. And Anselm Krauth is about to come face to face with the men he is sent to find....</p>
  <p class="closing">From the deadly streets of Budapest to the equally perilous corridors of Washington, Vrelska is an action-packed, compulsive thriller that depicts a financial scam terrifyingly close to reality.</p>
</section>

<section class="reviews">
  <h2>WHAT PEOPLE SAY</h2>
  <div class="card side left">
    <p class="quote">In a world ravaged by international turmoil and uncertainty for the future, author Marek Dunholt presents Vrelska, an intense and politically charged novel that is both timely and terrifying.”</p>
    <p class="cite">- Helen Marsby -</p>
  </div>
  <div class="card side right">
    <p class="quote">In a world ravaged by international turmoil and uncertainty for the future, author Marek Dunholt presents Vrelska, an intense and politically charged novel that is both timely and terrifying.”</p>
    <p class="cite">- Helen Marsby -</p>
  </div>
  <div class="card main">
    <p class="quote"><span class="qm">“</span> I give Vrelska by Marek Dunholt a definite four out of four stars. The action is fast paced so that it keeps you wanting to see what comes next. <span class="qm">”</span></p>
    <p class="cite">- ReadersCircle -</p>
  </div>
  <svg class="bubble" width="78" height="56" viewBox="0 0 78 56">
    <path d="M30 4 C14 4 4 12 4 22 C4 29 8 34 14 37 L10 47 L22 40 C25 41 27 41 30 41" fill="none" stroke="#4f9e86" stroke-width="4"/>
    <ellipse cx="50" cy="34" rx="25" ry="17" fill="#4f9e86"/>
    <path d="M60 48 L68 55 L64 44 Z" fill="#4f9e86"/>
    <rect x="34" y="27" width="32" height="2" fill="#b3e2d1"/>
    <rect x="34" y="33" width="32" height="2" fill="#b3e2d1"/>
    <rect x="34" y="39" width="32" height="2" fill="#b3e2d1"/>
  </svg>
  <div class="dots"><span></span><span class="active"></span><span></span><span></span></div>
</section>

<footer class="site-footer">© COPYRIGHT 2017 MAREK DUNHOLT - ALL RIGHTS RESERVED</footer>
<svg class="to-top" width="37" height="37" viewBox="0 0 37 37"><circle cx="18.5" cy="18.5" r="18.5" fill="#2d2d2d"/><path d="M18.5 10 V27 M13.5 15 L18.5 10 L23.5 15" stroke="#fff" stroke-width="2" fill="none"/></svg>
</body>
</html>
```